stationery for law firm in los angeles, CA
letterhead, envelope, business cards
stationery for law firm in los angeles, CA - Law
Creative Brief
Use specific fonts
I like these for example:Mercury,. Minion, Miller, Adobe Garamond, Sabon. Just examples,not required
Professional
Nadia Carrow
Attorney at Law
22817 Halvern Blvd. Suite 2600 Dellmont Park, CA 90268
Nadia@carrowlegal.test
www.carrowlegal.test
Please can you add Law Offices of Nadia L. Carrow on the stationery

```html
<!DOCTYPE html>
<html lang="en">
<head>
<meta charset="utf-8">
<title>Nadia Carrow – Attorney at Law – Business Card</title>
<link rel="stylesheet" href="https://fonts.googleapis.com/css2?family=EB+Garamond:wght@400;700&family=Arimo:wght@400&display=swap">
<style>
  :root {
    --ink: #0b0b0b;
    --paper: #ffffff;
    --footer-text: #ffffff;
  }
  html, body {
    margin: 0;
    padding: 0;
    overflow: hidden;
    background: var(--paper);
  }
  .card {
    position: relative;
    width: 1200px;
    height: 686px;
    background: var(--ink);
    overflow: hidden;
  }
  .card-shapes {
    position: absolute;
    inset: 0;
  }
  .identity {
    position: absolute;
    left: 0;
    top: 0;
    width: 1200px;
    font-family: "EB Garamond", Georgia, serif;
    color: var(--ink);
  }
  .attorney-name {
    position: absolute;
    left: 336px;
    top: 212px;
    margin: 0;
    font-size: 74px;
    font-weight: 700;
    line-height: 1;
    letter-spacing: 0.5px;
    white-space: nowrap;
  }
  .attorney-title {
    position: absolute;
    left: 256px;
    top: 278px;
    margin: 0;
    font-size: 100px;
    font-weight: 400;
    line-height: 1;
    white-space: nowrap;
  }
  .attorney-title .title-small {
    font-size: 50px;
    letter-spacing: 1px;
    margin: 0 10px 0 8px;
  }
  .firm-line {
    position: absolute;
    left: 652px;
    top: 392px;
    margin: 0;
    font-size: 24px;
    letter-spacing: 0.3px;
    text-transform: uppercase;
    white-space: nowrap;
  }
  .contact {
    position: absolute;
    top: 592px;
    margin: 0;
    font-family: "Arimo", Arial, sans-serif;
    font-style: normal;
    font-size: 19px;
    line-height: 24px;
    color: var(--footer-text);
  }
  .contact-office { left: 43px; text-align: left; }
  .contact-direct { right: 50px; text-align: right; }
</style>
</head>
<body>
  <main class="card">
    <svg class="card-shapes" width="1200" height="686" viewBox="0 0 1200 686" aria-hidden="true">
      <polygon points="360,0 1200,0 1200,540 0,555 0,252" fill="var(--paper)"/>
    </svg>

    <header class="identity">
      <h1 class="attorney-name">Nadia Carrow</h1>
      <p class="attorney-title">Attorney<span class="title-small">AT</span>Law</p>
      <p class="firm-line">Law Offices of Nadia L. Carrow</p>
    </header>

    <address class="contact contact-office">
      www.carrowlegal.test<br>
      22817 Halvern Blvd. Suite 2600<br>
      Dellmont Park, CA 90268
    </address>

    <address class="contact contact-direct">
      Email: nadia@carrowlegal.test<br>
      Phone: 818-555-0147<br>
      Fax: 310-555-0192
    </address>
  </main>
</body>
</html>
```